KVRo Business Cards

We need a business card design. We are a Technology (Audio Visual) design, sales and installation company. Looking for a double sided design, clean

Contact Information for Business Card

Clean, modern look, 2 sided

Font styles to use
Sans Serif

```html
<!DOCTYPE html>
<html lang="en">
<head>
<meta charset="utf-8">
<title>KVRo Business Cards</title>
<link rel="stylesheet" href="https://fonts.googleapis.com/css2?family=Arimo:wght@400;700&family=Oswald:wght@500&display=swap">
<style>
  :root {
    --page: #2a2a2a;
    --card: #161616;
    --white: #ffffff;
    --orange: #f7931e;
    --grey: #a9a9a9;
    --rule: #6d6d6d;
    --dot: #5a5a5a;
  }
  * { box-sizing: border-box; margin: 0; padding: 0; }
  html, body {
    width: 1200px; height: 900px; overflow: hidden;
    background: var(--page);
    font-family: "Arimo", Arial, sans-serif;
  }
  .sheet {
    position: relative; width: 1200px; height: 900px;
    display: flex; flex-direction: column; align-items: center; justify-content: center; gap: 40px;
  }
  .card {
    position: relative; width: 700px; height: 400px;
    background: var(--card);
    box-shadow: 0 10px 30px rgba(0,0,0,.45);
  }
  /* front */
  .card-front { display: flex; flex-direction: column; align-items: center; justify-content: center; }
  .wordmark {
    font-family: "Arimo", Arial, sans-serif; font-weight: 700;
    font-size: 128px; letter-spacing: -2px; line-height: 1;
    color: var(--white);
  }
  .social-row { display: flex; align-items: center; gap: 12px; margin-top: 40px; }
  .social-row .rule { width: 110px; height: 1px; background: var(--rule); }
  .social-row .dot { width: 34px; height: 34px; border-radius: 50%; background: var(--dot); }
  .social-row .dots { display: flex; gap: 8px; }
  /* back */
  .identity { position: absolute; right: 382px; top: 150px; text-align: right; }
  .person-name {
    font-family: "Oswald", sans-serif; font-weight: 500;
    font-size: 40px; line-height: 1; letter-spacing: .5px;
    color: var(--orange); text-transform: uppercase;
  }
  .person-title { font-size: 22px; color: var(--grey); margin-top: 6px; }
  .divider { position: absolute; left: 342px; top: 150px; width: 1px; height: 90px; background: var(--grey); }
  .contacts { position: absolute; left: 368px; top: 150px; list-style: none; }
  .contacts li { display: flex; align-items: center; gap: 10px; font-size: 21px; color: var(--grey); height: 30px; }
  .contacts svg { width: 22px; height: 22px; flex: none; }
  .address { position: absolute; left: 0; right: 0; bottom: 72px; text-align: center; font-size: 21px; color: var(--grey); }
</style>
</head>
<body>
<main class="sheet">
  <section class="card card-front" aria-label="Card front">
    <div class="wordmark">KVRo</div>
    <div class="social-row">
      <span class="rule"></span>
      <span class="dots"><span class="dot"></span><span class="dot"></span><span class="dot"></span></span>
      <span class="rule"></span>
    </div>
  </section>

  <section class="card card-back" aria-label="Card back">
    <div class="identity">
      <h1 class="person-name">Dana Whitlow</h1>
      <p class="person-title">Managing Director</p>
    </div>
    <span class="divider"></span>
    <ul class="contacts">
      <li>
        <svg viewBox="0 0 24 24" aria-hidden="true"><path fill="var(--orange)" d="M6.6 10.8a15.1 15.1 0 0 0 6.6 6.6l2.2-2.2c.3-.3.7-.4 1-.2 1.1.4 2.3.6 3.6.6.6 0 1 .4 1 1V20c0 .6-.4 1-1 1A17 17 0 0 1 3 4c0-.6.4-1 1-1h3.5c.6 0 1 .4 1 1 0 1.3.2 2.5.6 3.6.1.3 0 .7-.2 1z"/></svg>
        (555)201-4830
      </li>
      <li>
        <svg viewBox="0 0 24 24" aria-hidden="true"><rect x="2" y="5" width="20" height="14" fill="var(--orange)"/><path d="M2 5l10 8 10-8" fill="none" stroke="var(--card)" stroke-width="1.6"/></svg>
        sales@kvro.tech
      </li>
      <li>
        <svg viewBox="0 0 24 24" aria-hidden="true"><g fill="none" stroke="var(--orange)" stroke-width="1.8"><circle cx="12" cy="12" r="9"/><ellipse cx="12" cy="12" rx="4" ry="9"/><path d="M3 12h18M5 7h14M5 17h14"/></g></svg>
        www.kvro.tech
      </li>
    </ul>
    <p class="address">1180 Larkspur Ct.Suite 200, Maple Ridge, Georgia 30000</p>
  </section>
</main>
</body>
</html>
```